Lorena Bastow DDS PA Postcard Advertisement

Dr. Lorena Bastow Family Dentistry
*Following Needs to Stand Out*
• Free whiting for new patient ( with routine exam, cleaning and x-rays)
• Our Goal is to provide you with a pleasant, stress-free experience
• Accepting New Patients
• We file your insurance claims
• Schedule your appointment Today! Don’t contribute to the millions of dollars in dental benefits that go unused each year.
Contact Info
412 Fenwick Lane
Alderbrook, WV 28341
828-555-0147
Email: lbastowdds@pelmora.net
“Look for us on Facebook”

Attached files that can be used or just give ideas
Dr Bastow with her horse Wendell (one cropped and the other un-cropped)
These logo are examples of what she likes. They do not belong to her, she likes the dental tree designs. She loves the outdoors and nature.
This postcard will be used as a PSRV advertisement. Attached are they required layouts.

BOTH Front and Back can be used (full color)

The postcard size will be 11x6inches or 279.4mm x 152.4mm

Requirements
Must have
• *Following Needs to Stand Out*
• Accepting New Patients

```html
<!DOCTYPE html>
<html lang="en">
<head>
<meta charset="utf-8">
<title>Dr. Lorena Bastow Family Dentistry – Postcard</title>
<link href="https://fonts.googleapis.com/css2?family=Oswald:wght@600;700&family=Open+Sans:wght@400;700&display=swap" rel="stylesheet">
<style>
  :root {
    --blue-deep: #1f3a9e;
    --blue-mid: #2b5cc8;
    --blue-bright: #2f8fe0;
    --white: #ffffff;
    --photo-left-a: #6b5a4c;
    --photo-left-b: #3d3128;
    --leaf-a: #e0611e;
    --leaf-b: #b8420f;
    --leaf-dark: #3b2418;
  }
  * { margin: 0; padding: 0; box-sizing: border-box; }
  html, body { width: 1200px; height: 655px; overflow: hidden; background: var(--white); }
  .postcard {
    position: relative;
    width: 1200px;
    height: 655px;
    overflow: hidden;
    font-family: "Open Sans", Arial, sans-serif;
    color: var(--white);
  }
  .backdrop { position: absolute; inset: 0; }

  .headline {
    position: absolute;
    right: 36px;
    top: 30px;
    text-align: right;
    font-family: "Oswald", "Arial Narrow", sans-serif;
    font-weight: 700;
    font-size: 52px;
    line-height: 52px;
    letter-spacing: -0.5px;
    text-shadow: 0 2px 4px rgba(0,0,0,0.35);
  }
  .headline .today { text-transform: uppercase; }

  .offers {
    position: absolute;
    left: 650px;
    top: 220px;
    width: 514px;
    list-style: none;
  }
  .offer {
    height: 67px;
    margin-bottom: 29px;
    border-radius: 34px;
    background:
      linear-gradient(170deg, rgba(255,255,255,0.16) 0%, rgba(255,255,255,0) 48%),
      linear-gradient(90deg, var(--blue-deep) 0%, var(--blue-mid) 55%, var(--blue-bright) 100%);
    box-shadow: 0 2px 6px rgba(0,0,0,0.35);
    display: flex;
    flex-direction: column;
    justify-content: center;
    align-items: center;
    text-align: center;
  }
  .offer-title { font-weight: 700; font-size: 18.5px; line-height: 24px; }
  .offer-note { font-weight: 400; font-size: 18px; line-height: 22px; }

  .practice {
    position: absolute;
    left: 37px;
    top: 482px;
    font-style: normal;
  }
  .practice-name { font-weight: 700; font-size: 20.5px; line-height: 30px; }
  .practice-line { font-weight: 400; font-size: 20.5px; line-height: 28px; }

  .social {
    position: absolute;
    left: 37px;
    top: 582px;
    display: flex;
    align-items: center;
    gap: 10px;
  }
  .social-square { width: 38px; height: 38px; background: var(--blue-deep); }
  .social-handle { font-weight: 700; font-size: 18.5px; }
</style>
</head>
<body>
<div class="postcard">
  <svg class="backdrop" width="1200" height="655" viewBox="0 0 1200 655">
    <defs>
      <linearGradient id="leafTones" x1="0" y1="0" x2="1" y2="1">
        <stop offset="0" stop-color="var(--leaf-dark)"/>
        <stop offset="0.3" stop-color="var(--leaf-a)"/>
        <stop offset="0.65" stop-color="var(--leaf-b)"/>
        <stop offset="1" stop-color="var(--leaf-a)"/>
      </linearGradient>
      <linearGradient id="portraitTones" x1="0" y1="0" x2="1" y2="0">
        <stop offset="0" stop-color="var(--photo-left-a)"/>
        <stop offset="0.5" stop-color="var(--photo-left-b)"/>
        <stop offset="1" stop-color="#8a7a6a"/>
      </linearGradient>
      <linearGradient id="panelFade" x1="0" y1="0" x2="0" y2="1">
        <stop offset="0.5" stop-color="var(--blue-mid)" stop-opacity="0"/>
        <stop offset="0.75" stop-color="var(--blue-mid)" stop-opacity="0.85"/>
        <stop offset="1" stop-color="var(--blue-bright)" stop-opacity="1"/>
      </linearGradient>
    </defs>

    <rect class="leaf-photo" x="0" y="0" width="1200" height="655" fill="url(#leafTones)"
          role="img" aria-label="Photo of orange autumn maple leaves"/>

    <path class="swoosh-outer" d="M410,0 C380,170 400,320 480,450 C530,535 580,600 612,655 L0,655 L0,0 Z" fill="var(--blue-deep)"/>
    <path class="swoosh-inner" d="M398,0 C368,170 386,320 464,450 C512,535 560,600 590,655 L0,655 L0,0 Z" fill="var(--blue-bright)"/>

    <path class="portrait-photo" d="M392,0 C362,170 378,320 454,450 C500,535 548,600 576,655 L0,655 L0,0 Z"
          fill="url(#portraitTones)" role="img"
          aria-label="Photo of Dr. Lorena Bastow standing with her horse Wendell"/>
    <path class="panel-fade" d="M392,0 C362,170 378,320 454,450 C500,535 548,600 576,655 L0,655 L0,0 Z" fill="url(#panelFade)"/>
  </svg>

  <h1 class="headline">Schedule<br>your appointment<br><span class="today">Today!</span></h1>

  <ul class="offers">
    <li class="offer">
      <span class="offer-title">Free Whitening for New Patients</span>
      <span class="offer-note">(with Routine Exam, Cleaning and X-rays)</span>
    </li>
    <li class="offer">
      <span class="offer-title">Our Goal is to Provide You and You’re Family</span>
      <span class="offer-note">with a Pleasant, Stress-Free Experience</span>
    </li>
    <li class="offer">
      <span class="offer-title">ACCEPTING NEW PATIENTS</span>
    </li>
    <li class="offer">
      <span class="offer-title">WE FILE YOUR INSURANCE CLAIMS</span>
    </li>
  </ul>

  <address class="practice">
    <div class="practice-name">Dr. Lorena Bastow Family Dentistry</div>
    <div class="practice-line">412 Fenwick Lane, Alderbrook, WV 28341</div>
    <div class="practice-line">555-210-0147 | lbastowdds@pelmora.net</div>
  </address>

  <div class="social">
    <span class="social-square"></span>
    <span class="social-handle">LorenaBastowDDS</span>
  </div>
</div>
</body>
</html>
```